24/7 Gym Membership Pricing Card (A6)

I need a pricing card with the different membership options on it.

The membership options are;

12 Month Minimum Term:
No Joining Fee, $25 Access Card Fee, $12.25 per week

No Contract:
$89 Joining Fee, $55 Access Card Fee, $13.50 per week

Pay in Advance:
12 Month - $540
6 Month - $295
3 Month - $190

I have attached our old pricing card below for reference.

Our Logo is also attached.

Target Market(s)

Potential members

Industry/Entity Type

Fitness

Colors
f37122
f68e4e
f9bb94
f78f20
faa54b
fbc994

Requirements
Must have
• My Logo, pricing options
Nice to have
• Contact details; 4158 2293, hollis@vantorafit.com.au, www.vantorafit.com.au
• Our staffed hours; Mon-Thur: 12pm - 7pm, Fri-Sat: 8am - 1pm
Should not have
• Wasted space

```html
<!DOCTYPE html>
<html lang="en">
<head>
<meta charset="utf-8">
<title>Vantora Fit Hollis – Membership Pricing Card</title>
<link rel="stylesheet" href="https://fonts.googleapis.com/css2?family=Oswald:wght@400;500;700&family=Roboto+Condensed:wght@400;700&display=swap">
<style>
  :root {
    --orange: #f37122;
    --orange-mid: #f78f20;
    --orange-light: #faa54b;
    --orange-pale: #fbc994;
    --charcoal: #3d3d3f;
    --charcoal-dark: #2e2e30;
    --ink: #1c1c1c;
    --white: #ffffff;
    --ring: #8a8d92;
    --backdrop: #dfe3e6;
  }
  * { box-sizing: border-box; margin: 0; padding: 0; }
  html, body { width: 1200px; height: 1037px; overflow: hidden; }
  body {
    background: var(--backdrop);
    font-family: "Roboto Condensed", "Arial Narrow", sans-serif;
    position: relative;
  }
  .card {
    position: absolute;
    left: 260px; top: 38px;
    width: 680px; height: 962px;
    background: var(--white);
    overflow: hidden;
  }
  .hero-photo {
    position: absolute; left: 0; top: 0; width: 680px; height: 760px;
    background:
      linear-gradient(100deg, rgba(255,255,255,.55) 0%, rgba(255,255,255,0) 35%),
      linear-gradient(160deg, #cfd2d5 0%, #9ea3a8 35%, #6e7379 60%, #b9bcbf 80%, #e6e6e6 100%);
  }
  .title-banner {
    position: absolute; right: 0; top: 0;
    width: 360px; height: 86px;
    background: var(--charcoal);
    clip-path: polygon(60px 0, 100% 0, 100% 100%, 0 100%);
    display: flex; align-items: center; justify-content: flex-end;
    padding-right: 28px;
  }
  .title-banner h1 {
    font-family: "Oswald", sans-serif; font-weight: 700;
    color: var(--white); font-size: 44px; letter-spacing: .5px;
  }
  .plan {
    position: absolute; width: 170px;
    background: var(--white);
    padding: 14px 10px 16px;
    box-shadow: 0 4px 10px rgba(0,0,0,.25);
  }
  .plan-1 { left: 30px; top: 40px; }
  .plan-2 { left: 215px; top: 118px; }
  .plan-3 { left: 400px; top: 196px; }
  .plan h2 {
    font-family: "Oswald", sans-serif; font-weight: 700;
    font-size: 20px; line-height: 21px; text-align: center;
    color: var(--ink); text-transform: uppercase;
    margin-bottom: 14px;
  }
  .price-tag {
    height: 120px;
    border-radius: 4px;
    position: relative;
    display: flex; flex-direction: column; align-items: center; justify-content: center;
    color: var(--ink);
    box-shadow: 0 2px 3px rgba(0,0,0,.25);
  }
  .price-tag::before {
    content: ""; position: absolute; inset: 6px;
    border: 1.5px dashed rgba(255,255,255,.6); border-radius: 3px;
  }
  .tone-1 { background: linear-gradient(180deg, var(--orange-light), var(--orange-mid)); }
  .tone-2 { background: linear-gradient(180deg, var(--orange-mid), #f47f21); }
  .tone-3 { background: linear-gradient(180deg, #f47a22, var(--orange)); }
  .amount {
    font-family: "Oswald", sans-serif; font-weight: 700;
    font-size: 36px; line-height: 38px;
  }
  .amount sup { font-size: 18px; vertical-align: 14px; }
  .label {
    font-size: 14px; line-height: 15px; text-transform: uppercase; text-align: center;
  }
  .rings {
    height: 14px; display: flex; justify-content: space-evenly; padding: 0 14px;
    position: relative; z-index: 1;
  }
  .rings span {
    width: 7px; height: 22px; margin-top: -4px;
    border: 2px solid var(--ring); border-radius: 4px;
    background: transparent;
  }
  .hours-strip {
    position: absolute; left: 0; top: 760px; width: 680px; height: 80px;
    background: var(--white);
    display: flex; align-items: center; justify-content: flex-end;
    padding-right: 30px; gap: 16px;
  }
  .hours-title {
    font-family: "Oswald", sans-serif; font-weight: 500; font-size: 19px;
    line-height: 19px; text-align: right; color: var(--ink); text-transform: uppercase;
  }
  .hours-table { font-size: 15px; line-height: 19px; color: var(--ink); border-collapse: collapse; }
  .hours-table td { padding: 0 8px; }
  .brand-block {
    position: absolute; left: 0; top: 742px; width: 270px; height: 98px;
    background: var(--orange);
    clip-path: polygon(0 0, 210px 0, 100% 100%, 0 100%);
    display: flex; align-items: center; padding-left: 38px; gap: 10px;
    color: var(--white);
  }
  .brand-dot { width: 22px; height: 22px; border-radius: 50%; background: var(--white); }
  .brand-name {
    font-family: "Oswald", sans-serif; font-weight: 500; font-size: 24px; line-height: 24px;
  }
  .brand-name small { display: block; font-size: 13px; letter-spacing: 4px; line-height: 18px; }
  .contact-band {
    position: absolute; left: 0; top: 840px; width: 680px; height: 106px;
    background: linear-gradient(180deg, var(--charcoal), var(--charcoal-dark));
    color: var(--white);
    display: flex; flex-direction: column; align-items: center; justify-content: center;
    font-family: "Oswald", sans-serif; font-weight: 400; font-size: 25px; line-height: 36px;
  }
  .accent-rule {
    position: absolute; left: 0; top: 946px; width: 680px; height: 16px;
    background: var(--orange);
  }
</style>
</head>
<body>
  <main class="card">
    <div class="hero-photo" role="img" aria-label="Gym photo of a woman lifting dumbbells on a bench with a spotter"></div>

    <header class="title-banner"><h1>MEMBERSHIP</h1></header>

    <section class="plan plan-1">
      <h2>12 Month<br>Minimum<br>Term</h2>
      <div class="price-tag tone-1"><span class="amount">NO</span><span class="label">Joining Fee</span></div>
      <div class="rings"><span></span><span></span><span></span><span></span></div>
      <div class="price-tag tone-2"><span class="amount"><sup>$</sup>25</span><span class="label">Access<br>Card Fee</span></div>
      <div class="rings"><span></span><span></span><span></span><span></span></div>
      <div class="price-tag tone-3"><span class="amount"><sup>$</sup>12.25</span><span class="label">Per Week</span></div>
    </section>

    <section class="plan plan-2">
      <h2>No<br>Contract</h2>
      <div class="price-tag tone-1"><span class="amount"><sup>$</sup>89</span><span class="label">Joining Fee</span></div>
      <div class="rings"><span></span><span></span><span></span><span></span></div>
      <div class="price-tag tone-2"><span class="amount"><sup>$</sup>55</span><span class="label">Access<br>Card Fee</span></div>
      <div class="rings"><span></span><span></span><span></span><span></span></div>
      <div class="price-tag tone-3"><span class="amount"><sup>$</sup>13.50</span><span class="label">Per Week</span></div>
    </section>

    <section class="plan plan-3">
      <h2>Pay In<br>Advance</h2>
      <div class="price-tag tone-1"><span class="amount"><sup>$</sup>540</span><span class="label">12 Month</span></div>
      <div class="rings"><span></span><span></span><span></span><span></span></div>
      <div class="price-tag tone-2"><span class="amount"><sup>$</sup>295</span><span class="label">6 Month</span></div>
      <div class="rings"><span></span><span></span><span></span><span></span></div>
      <div class="price-tag tone-3"><span class="amount"><sup>$</sup>190</span><span class="label">3 Month</span></div>
    </section>

    <section class="hours-strip">
      <p class="hours-title">Our<br>Staffed Hours</p>
      <table class="hours-table">
        <tr><td>Monday-Thursday</td><td>12pm - 7pm</td></tr>
        <tr><td>Friday-Saturday</td><td>8am - 1pm</td></tr>
      </table>
    </section>

    <div class="brand-block">
      <span class="brand-dot"></span>
      <p class="brand-name">Vantora Fit<small>HOLLIS</small></p>
    </div>

    <footer class="contact-band">
      <p>4158 2293, hollis@vantorafit.com.au</p>
      <p>www.vantorafit.com.au</p>
    </footer>
    <div class="accent-rule"></div>
  </main>
</body>
</html>
```